ROLLFAST FITNESSRoll Out, A UNIQUE CONCIERGE MOBILE SERVICE LAUNCHING in SOUTH FLORIDA

I AM LOOKING TO ATTRACT LEADS FOR CONVERSION WHILE BRINGING OUR SERVICE TO LIFE IN THERE HANDS. WE SERVICE A VERY HIGHLY AFFLUENT CROWD. I would like those on a 5 x 7 two sided card

Target Market(s)

AFFLUENT

Industry/Entity Type

HEALTH AND FITNESS

Font styles to use
Other font styles liked:
• POPINS MED

Colors
0054AA
0677BA
7BADD7
CADEEF
E8F1F8
FFF300
FFF600
FEFA6F
FFFEC7
FFFEE8

Requirements
Must have
• space for postage I INCLUDED CONTENT
Nice to have
• CLASSY FUN LOOK
Should not have
• DULLNESs

```html
<!DOCTYPE html>
<html lang="en">
<head>
<meta charset="utf-8">
<title>BriskWave Fitness – Postcard Front and Back</title>
<link rel="stylesheet" href="https://fonts.googleapis.com/css2?family=Poppins:wght@400;500;600;700;800&display=swap">
<style>
  :root {
    --cyan: #66c8d8;
    --cyan-deep: #4fb7c9;
    --yellow: #fff300;
    --ink: #3a3d42;
    --ink-soft: #55595f;
    --paper: #ffffff;
    --stage: #e6e9ec;
    --line: #c9ccd0;
  }
  * { box-sizing: border-box; margin: 0; padding: 0; }
  html, body { width: 1200px; height: 900px; overflow: hidden; }
  body {
    background: var(--stage);
    font-family: "Poppins", sans-serif;
    display: flex;
    align-items: center;
    justify-content: center;
    gap: 20px;
  }
  .postcard {
    position: relative;
    width: 570px;
    height: 407px;
    background: var(--paper);
    overflow: hidden;
    box-shadow: 0 6px 18px rgba(0,0,0,.18);
  }
  .postcard > svg.card-art { position: absolute; inset: 0; }

  .brand-name {
    position: absolute;
    font-weight: 700;
    color: var(--cyan);
    line-height: 1;
    white-space: nowrap;
  }
  .web-pill {
    position: absolute;
    display: flex;
    align-items: center;
    height: 30px;
    padding: 0 16px 0 40px;
    background: var(--cyan);
    border-radius: 15px;
    color: #fff;
    font-weight: 500;
    font-size: 15px;
    white-space: nowrap;
  }
  .web-pill .globe {
    position: absolute;
    left: -4px;
    top: -2px;
    width: 34px;
    height: 34px;
    border-radius: 50%;
    background: var(--ink);
    border: 3px solid #fff;
    display: flex;
    align-items: center;
    justify-content: center;
  }

  /* Front */
  .front .brand-name { left: 36px; top: 108px; font-size: 19px; }
  .front .headline {
    position: absolute;
    left: 36px;
    top: 150px;
    width: 300px;
    font-weight: 700;
    font-size: 22px;
    line-height: 1.2;
    color: var(--ink);
  }
  .front .service-line {
    position: absolute;
    left: 36px;
    top: 240px;
    width: 230px;
    font-size: 11px;
    line-height: 1.45;
    color: var(--ink-soft);
  }
  .front .web-pill { left: 40px; top: 300px; }

  /* Back */
  .back .headline {
    position: absolute;
    left: 22px;
    top: 262px;
    width: 220px;
    font-weight: 700;
    font-size: 15px;
    line-height: 1.2;
    color: #fff;
  }
  .back .mobile-badge {
    position: absolute;
    left: 216px;
    top: 222px;
    width: 78px;
    height: 78px;
    border-radius: 50%;
    background: var(--yellow);
    border: 4px solid #fff;
    display: flex;
    align-items: center;
    justify-content: center;
    text-align: center;
    color: #fff;
    font-weight: 700;
    font-size: 12px;
    line-height: 1.1;
  }
  .back .brand-name { left: 300px; top: 62px; font-size: 16px; }
  .back .web-pill { left: 352px; top: 322px; font-size: 14px; }
  .back .closing {
    position: absolute;
    left: 22px;
    top: 360px;
    font-size: 11px;
    line-height: 1.35;
    color: var(--ink);
  }
  .back .closing strong { font-weight: 700; display: block; }
</style>
</head>
<body>

  <section class="postcard front">
    <svg class="card-art" width="570" height="407" viewBox="0 0 570 407">
      <defs>
        <linearGradient id="frontPhotoTone" x1="0" y1="0" x2="1" y2="1">
          <stop offset="0" stop-color="#9aa1a6"/>
          <stop offset=".55" stop-color="#6f757b"/>
          <stop offset="1" stop-color="#b9b1a8"/>
        </linearGradient>
        <linearGradient id="frontInsetTone" x1="0" y1="0" x2="1" y2="1">
          <stop offset="0" stop-color="#c8ced3"/>
          <stop offset="1" stop-color="#5f656b"/>
        </linearGradient>
      </defs>
      <polygon class="accent-cyan" points="150,0 300,0 262,130" fill="var(--cyan)"/>
      <polygon class="accent-yellow" points="262,130 300,0 320,0 300,170" fill="var(--yellow)"/>
      <path class="hero-photo" role="img" aria-label="Photo: woman training with resistance bands beside the branded fitness truck"
            d="M300,0 H570 V290 L330,380 L342,248 Q346,222 328,204 L300,170 Z" fill="url(#frontPhotoTone)"/>
      <polygon class="band-yellow" points="250,407 330,380 570,290 570,318 360,407" fill="var(--yellow)"/>
      <polygon class="band-cyan" points="360,407 570,318 570,326 380,407" fill="var(--cyan)"/>
      <polygon class="wedge-yellow" points="250,407 300,320 345,300 330,380" fill="var(--yellow)"/>
      <circle cx="328" cy="318" r="52" fill="#fff"/>
      <circle class="inset-photo" role="img" aria-label="Photo: the fitness truck parked on a rooftop" cx="328" cy="318" r="46" fill="url(#frontInsetTone)"/>
      <circle cx="328" cy="318" r="49" fill="none" stroke="var(--yellow)" stroke-width="1.5"/>
      <g class="chevrons" fill="none" stroke-width="4" stroke-linejoin="miter">
        <polyline points="50,358 62,370 50,382" stroke="var(--cyan)"/>
        <polyline points="62,358 74,370 62,382" stroke="var(--yellow)"/>
        <polyline points="74,358 86,370 74,382" stroke="var(--cyan)"/>
        <polyline points="86,358 98,370 86,382" stroke="var(--yellow)"/>
        <polyline points="98,358 110,370 98,382" stroke="var(--cyan)"/>
        <polyline points="110,358 122,370 110,382" stroke="var(--yellow)"/>
        <polyline points="122,358 134,370 122,382" stroke="var(--cyan)"/>
      </g>
    </svg>

    <div class="brand-name">BRISKWAVE FITNESS</div>
    <h1 class="headline">GET FIT ON YOUR SCHEDULE, ANYWHERE, ANYTIME</h1>
    <p class="service-line">The Ultimate Mobile Concierge Fitness Service for Health, Golf, Tennis, Flexibility, Strength, and Agility</p>
    <div class="web-pill">
      <span class="globe">
        <svg width="16" height="16" viewBox="0 0 16 16" fill="none" stroke="#fff" stroke-width="1.2">
          <circle cx="8" cy="8" r="6.5"/><ellipse cx="8" cy="8" rx="3" ry="6.5"/><line x1="1.5" y1="8" x2="14.5" y2="8"/>
        </svg>
      </span>
      briskwavefitness.com
    </div>
  </section>

  <section class="postcard back">
    <svg class="card-art" width="570" height="407" viewBox="0 0 570 407">
      <defs>
        <linearGradient id="backPhotoTone" x1="0" y1="0" x2="1" y2="1">
          <stop offset="0" stop-color="#d4d8db"/>
          <stop offset=".5" stop-color="#7b8187"/>
          <stop offset="1" stop-color="#8a6f68"/>
        </linearGradient>
        <linearGradient id="groupPhotoTone" x1="0" y1="0" x2="1" y2="1">
          <stop offset="0" stop-color="#b9dbe6"/>
          <stop offset="1" stop-color="#a77f95"/>
        </linearGradient>
      </defs>
      <path class="hero-photo" role="img" aria-label="Photo: two clients doing suspension and band training at the fitness truck"
            d="M0,40 L250,0 Q282,-5 290,20 L300,110 Q304,140 290,170 L250,260 L0,300 Z" fill="url(#backPhotoTone)"/>
      <polygon class="accent-yellow" points="268,220 290,170 300,190 282,232" fill="var(--yellow)"/>
      <path class="headline-panel" d="M0,250 Q60,230 120,238 L235,250 L270,330 L0,352 Z" fill="var(--cyan)"/>
      <polygon class="band-yellow" points="0,352 570,290 570,300 0,360" fill="var(--yellow)"/>
      <polygon class="band-cyan" points="270,330 570,290 570,296 275,336" fill="var(--cyan-deep)"/>
      <g class="panel-arrows" fill="none" stroke-width="4">
        <polyline points="24,240 36,250 24,260" stroke="#fff"/>
        <polyline points="34,240 46,250 34,260" stroke="var(--yellow)"/>
      </g>
      <circle cx="330" cy="270" r="50" fill="#fff"/>
      <circle class="group-photo" role="img" aria-label="Photo: cheerful group of clients after a rooftop class" cx="330" cy="270" r="45" fill="url(#groupPhotoTone)"/>
      <circle cx="330" cy="270" r="47.5" fill="none" stroke="var(--yellow)" stroke-width="1.5"/>
      <rect class="stamp-box" x="478" y="14" width="76" height="82" fill="none" stroke="var(--line)" stroke-width="1.2"/>
      <g class="address-lines" stroke="var(--line)" stroke-width="1">
        <line x1="330" y1="140" x2="555" y2="140"/>
        <line x1="330" y1="175" x2="555" y2="175"/>
        <line x1="330" y1="210" x2="555" y2="210"/>
        <line x1="390" y1="245" x2="555" y2="245"/>
      </g>
    </svg>

    <h2 class="headline">TRANSFORM YOUR BODY AND YOUR GAME WITH BRISKWAVE FITNESS</h2>
    <div class="mobile-badge">MOBILE<br>SERVICE</div>
    <div class="brand-name">BRISKWAVE FITNESS</div>
    <div class="web-pill">
      <span class="globe">
        <svg width="16" height="16" viewBox="0 0 16 16" fill="none" stroke="#fff" stroke-width="1.2">
          <circle cx="8" cy="8" r="6.5"/><ellipse cx="8" cy="8" rx="3" ry="6.5"/><line x1="1.5" y1="8" x2="14.5" y2="8"/>
        </svg>
      </span>
      briskwavefitness.com
    </div>
    <p class="closing">Conclusion: Get Started with BriskWave Fitness Today
      <strong>FOR FREE CONSULTAION AND ASSESMENT GO TO:</strong></p>
  </section>

</body>
</html>
```